Telmoro Business Card

I already have the conplay logo. I need to develop a professional business card layout

Target Market(s)

Business

Industry/Entity Type

Business

Contact Information for Business Card

Company Name: Telmoro Limited

Font styles to use
Sans Serif

Colors

Designer to choose colors to be used in the design.

Requirements
Must have
• Use current logo
• Need two card size options:
• Small Card: 70mm x 28mm (Landscape)
• Square Card: 65mm x 65mm
Nice to have
• I will need 8-10 files for each name, number and email address (details to follow)

```html
<!DOCTYPE html>
<html lang="en">
<head>
<meta charset="utf-8">
<title>Telmoro Business Card</title>
<link rel="stylesheet" href="https://fonts.googleapis.com/css2?family=Lato:wght@300;400;900&family=Oswald:wght@200&family=Roboto+Condensed:wght@400&display=swap">
<style>
  :root {
    --paper: #ffffff;
    --ink: #111111;
    --brand: #7a1fe0;
    --violet-deep: #5a0fc8;
    --violet: #a020f0;
    --violet-light: #d65cf5;
    --red: #e8103a;
    --rose: #f0285a;
    --orange: #ff6a14;
  }
  html, body {
    margin: 0;
    padding: 0;
    width: 1200px;
    height: 1200px;
    overflow: hidden;
    background: var(--paper);
  }
  .card {
    position: relative;
    width: 1200px;
    height: 1200px;
    background: var(--paper);
    overflow: hidden;
  }
  .facets {
    position: absolute;
    inset: 0;
    width: 1200px;
    height: 1200px;
  }
  .brand-name {
    position: absolute;
    right: 44px;
    top: 170px;
    margin: 0;
    font-family: "Lato", sans-serif;
    font-weight: 900;
    font-size: 122px;
    line-height: 1;
    letter-spacing: 0.01em;
    color: var(--brand);
  }
  .brand-legal {
    position: absolute;
    right: 95px;
    top: 293px;
    margin: 0;
    font-family: "Lato", sans-serif;
    font-weight: 400;
    font-size: 25px;
    line-height: 1;
    color: var(--ink);
  }
  .person-name {
    position: absolute;
    right: 56px;
    top: 402px;
    margin: 0;
    font-family: "Oswald", sans-serif;
    font-weight: 200;
    font-size: 104px;
    line-height: 1.1;
    letter-spacing: 0.24em;
    margin-right: -0.24em;
    color: var(--ink);
  }
  .person-role {
    position: absolute;
    right: 78px;
    top: 513px;
    margin: 0;
    font-family: "Lato", sans-serif;
    font-weight: 300;
    font-size: 50px;
    line-height: 1;
    color: var(--ink);
  }
  .contact-line {
    position: absolute;
    right: 220px;
    margin: 0;
    font-family: "Roboto Condensed", sans-serif;
    font-weight: 400;
    font-size: 42px;
    line-height: 45px;
    text-align: right;
    color: var(--ink);
  }
  .contact-address { top: 690px; }
  .contact-phone { top: 852px; }
  .contact-email { top: 970px; }
  .contact-icon {
    position: absolute;
    left: 1058px;
    width: 62px;
    height: 62px;
    fill: var(--ink);
  }
  .icon-home { top: 705px; }
  .icon-phone { top: 840px; }
  .icon-mail { top: 962px; }
</style>
</head>
<body>
<main class="card">
  <svg class="facets" viewBox="0 0 1200 1200" aria-hidden="false">
    <defs>
      <linearGradient id="violet-field" x1="0" y1="0" x2="1" y2="1">
        <stop offset="0" stop-color="var(--violet-deep)"/>
        <stop offset="0.5" stop-color="var(--violet)"/>
        <stop offset="1" stop-color="var(--violet-light)"/>
      </linearGradient>
      <linearGradient id="warm-field" x1="0" y1="0" x2="1" y2="0.4">
        <stop offset="0" stop-color="var(--red)"/>
        <stop offset="0.55" stop-color="var(--rose)"/>
        <stop offset="1" stop-color="var(--orange)"/>
      </linearGradient>
    </defs>
    <polygon role="img" aria-label="Violet low-poly facet pattern"
             fill="url(#violet-field)"
             points="0,0 609,0 156,305 305,336 47,484 148,633 0,780"/>
    <polygon role="img" aria-label="Red and orange low-poly facet pattern"
             fill="url(#warm-field)"
             points="0,766 125,859 148,992 578,1012 906,1200 0,1200"/>
  </svg>

  <h1 class="brand-name">TELMORO</h1>
  <p class="brand-legal">Telmoro Limited</p>

  <h2 class="person-name">KARL VANE</h2>
  <p class="person-role">Creative Director</p>

  <p class="contact-line contact-address">YOUR ADDRESS<br>STREET LOCATION, CITY</p>
  <svg class="contact-icon icon-home" viewBox="0 0 24 24" aria-hidden="true">
    <path d="M12 3 1.5 11.5 3 13l1.5-1.2V21h6v-6h3v6h6v-9.2L21 13l1.5-1.5L18 7.9V4h-3v1.5z"/>
  </svg>

  <p class="contact-line contact-phone">+92 0345 2218604</p>
  <svg class="contact-icon icon-phone" viewBox="0 0 24 24" aria-hidden="true">
    <path d="M6.6 2.5c.6-.4 1.4-.3 1.8.3l2.2 3.3c.4.6.3 1.3-.2 1.8L8.9 9.2c.9 2.3 3.5 5 5.9 5.9l1.3-1.5c.5-.5 1.2-.6 1.8-.2l3.3 2.2c.6.4.7 1.2.3 1.8l-1.4 2.1c-.6.9-1.7 1.3-2.8 1-6.4-1.8-11.4-6.8-13.2-13.2-.3-1.1.1-2.2 1-2.8z"/>
  </svg>

  <p class="contact-line contact-email">YOUR@MAILBOX.COM</p>
  <svg class="contact-icon icon-mail" viewBox="0 0 24 24" aria-hidden="true">
    <path d="M1 5h22v14H1zm2.2 1.5 8.8 7 8.8-7zM2.5 7.3v10l6.3-5zm19 0-6.3 5 6.3 5zM10 13.3l-6.8 4.2h17.6L14 13.3l-2 1.6z" fill-rule="evenodd"/>
  </svg>
</main>
</body>
</html>
```